Redesign start page for existing online shop

We are selling building material (chimneys and flue pipes) as well as fireplaces (stoves). For this online shop we need a new start page. The domain is brunnfeld-bauwaren.de. Here you can see the current design. We want a smoother design with just one banner in the middle instead of the three in the first row. The look has to be more professional and trustworthy. You can therefore play with the colors. We want to try some different orange instead of our yellow / orange color. A few more things: - The phone number has to be bigger and more highlighted - So the 5 advantages at the top should be shown in a different way - New design for the products below - New footer

Target Market(s)

Germany and other countries in Europe.

Industry/Entity Type

Home Builder

Number of Pages Required

1 page

Other font styles liked:
• Please se the font on our current site.

Colors
f78f20
f68d4c

Requirements
Must have
• - Clear design - Trustworthy look - All elements Which are now shown shoulderstand be still there after redesigning -
Nice to have
• - See the Following sites to have a clou about our wishes: kalvesto.de flinkrabe.de

```html
<!DOCTYPE html>
<html lang="en">
<head>
<meta charset="utf-8">
<title>Brunnfeld Bauwaren – Start page</title>
<link href="https://fonts.googleapis.com/css2?family=Open+Sans:wght@400;600;700&family=Roboto:wght@300;400;500;700&display=swap" rel="stylesheet">
<style>
:root{
  --orange:#f78f20;
  --orange-soft:#f68d4c;
  --ink:#333333;
  --muted:#777777;
  --line:#e3e3e3;
  --light:#f4f4f4;
  --slate:#4a5560;
  --footer:#2a2a2a;
  --footer-deep:#1c1c1c;
  --white:#ffffff;
}
*{margin:0;padding:0;box-sizing:border-box}
html,body{width:1200px;height:3789px;overflow:hidden}
body{font-family:"Open Sans",Arial,sans-serif;color:var(--ink);background:var(--white);position:relative;font-size:13px}
.wrap{width:1008px;margin:0 auto;position:relative}
a{color:inherit;text-decoration:none}
.btn{display:inline-block;background:var(--orange);color:var(--white);font-family:"Roboto",Arial,sans-serif;font-weight:500;text-transform:uppercase;border-radius:4px;letter-spacing:.5px}

/* top bar */
.topbar{height:45px;background:#f7f7f7;border-bottom:1px solid var(--line)}
.topbar .wrap{display:flex;align-items:center;height:45px;gap:10px}
.drop{border:1px solid #d6d6d6;background:var(--white);font-size:11px;padding:5px 12px;border-radius:3px;color:#555}
.drop::after{content:" ▾";font-size:9px}
.rating{margin-left:auto;display:flex;align-items:center;gap:4px;font-size:11px;color:#555}
.star{color:var(--orange);font-size:14px}
.account{font-size:11px;margin-left:26px;color:#555;text-transform:uppercase}
.cart{width:30px;height:30px;border-radius:50%;background:var(--orange);margin-left:14px;display:flex;align-items:center;justify-content:center}

/* header */
.header{height:112px;border-bottom:1px solid var(--line)}
.header .wrap{display:flex;align-items:center;height:112px}
.brand{display:flex;align-items:center;gap:12px}
.brand-mark{width:40px;height:40px;border-radius:50%;background:var(--orange)}
.brand-name{font-family:"Roboto",Arial,sans-serif;font-size:22px;font-weight:500;line-height:1.05;color:#3a3a3a;text-transform:uppercase}
.search{margin-left:132px;display:flex;width:380px;height:40px;border:1px solid #d0d0d0;border-radius:3px;overflow:hidden}
.search span{flex:1;padding:0 14px;line-height:38px;font-size:12px;color:#999}
.search i{width:42px;background:var(--orange);display:flex;align-items:center;justify-content:center}
.hotline{margin-left:auto;display:flex;align-items:center;gap:10px}
.hotline .ph{width:34px;height:34px;border-radius:50%;background:var(--orange);display:flex;align-items:center;justify-content:center}
.hotline b{display:block;font-family:"Roboto",Arial,sans-serif;font-size:20px;color:var(--orange);font-weight:500}
.hotline small{font-size:12px;color:#555}

/* nav */
.nav{height:60px;border-bottom:1px solid var(--line)}
.nav .wrap{display:flex;align-items:center;height:60px;font-family:"Roboto",Arial,sans-serif;font-size:14px;font-weight:500;text-transform:uppercase;color:#333}
.nav .item{margin-right:30px}
.nav .has-sub::after{content:" ▾";font-size:10px}
.nav .sep{margin-left:52px}
.nav .sep span{padding:0 10px;color:#aaa}
.seals{margin-left:auto;display:flex;gap:10px}
.seal{width:36px;height:36px;border-radius:50%;background:#3c3c3c}
.seal.sq{border-radius:3px;background:#e9e9e9;border:1px solid #ccc}

/* usp strip */
.usp{height:46px;background:var(--slate)}
.usp .wrap{display:flex;align-items:center;height:46px;gap:44px;color:var(--white);font-size:12px;font-weight:600;text-transform:uppercase}
.usp svg{vertical-align:-2px;margin-right:8px}

/* hero */
.hero{height:482px;position:relative;background:linear-gradient(180deg,#d8e6f2 0%,#b5c9dc 40%,#6d6560 62%,#4a3c36 100%);overflow:hidden}
.hero-photo{position:absolute;inset:0}
.hero-copy{position:absolute;left:732px;top:110px}
.hero-copy h1{font-family:"Roboto",Arial,sans-serif;font-weight:400;font-size:50px;color:var(--white);letter-spacing:1px}
.hero-copy .btn{margin-top:14px;padding:10px 18px;font-size:14px}
.dots{position:absolute;left:0;right:0;bottom:26px;display:flex;justify-content:center;gap:8px}
.dots i{width:11px;height:11px;border-radius:50%;background:var(--white)}
.dots i.on{background:var(--orange)}

/* brands */
.brands{height:96px;background:#f2f2f2;border-bottom:1px solid var(--line)}
.brands .wrap{display:flex;justify-content:space-between;align-items:center;height:96px;padding:0 44px}
.brands span{font-family:"Roboto",Arial,sans-serif;font-size:26px;font-weight:700;color:#9a9a9a;letter-spacing:1px}

/* features */
.features{height:346px}
.features .wrap{display:grid;grid-template-columns:repeat(4,1fr);gap:40px;padding:60px 30px 0}
.feature{text-align:center}
.ring{width:126px;height:126px;border-radius:50%;border:2px solid var(--orange-soft);margin:0 auto;display:flex;align-items:center;justify-content:center;background:var(--white)}
.feature h3{font-family:"Roboto",Arial,sans-serif;font-weight:400;font-size:16px;line-height:1.35;margin-top:26px;color:#333}
.feature p{font-size:11px;color:var(--muted);line-height:1.55;margin-top:10px}

/* how it works */
.how{height:556px;background:linear-gradient(160deg,#f6f6f6,#ebebeb);text-align:center;padding-top:96px}
.how h2{font-family:"Roboto",Arial,sans-serif;font-weight:500;font-size:32px;letter-spacing:1px}
.how .sub{font-size:14px;color:#555;margin-top:8px}
.steps{display:flex;justify-content:center;align-items:flex-start;margin-top:56px}
.step{width:200px}
.step .disc{width:121px;height:121px;border-radius:50%;background:var(--orange);margin:0 auto;display:flex;align-items:center;justify-content:center;box-shadow:0 0 0 6px rgba(247,143,32,.18)}
.step p{font-size:14px;color:#444;margin-top:18px;line-height:1.35}
.arrow{width:60px;padding-top:50px;font-size:24px;color:#555}
.how .cta{font-size:13px;color:#555;margin-top:36px}
.how .btn{margin-top:14px;padding:11px 22px;font-size:14px;border-radius:18px;text-transform:none}

/* products */
.products{height:581px;text-align:center;padding-top:50px}
.products h2{font-family:"Roboto",Arial,sans-serif;font-weight:500;font-size:36px}
.grid{display:grid;grid-template-columns:repeat(4,222px);gap:40px;justify-content:center;margin-top:32px}
.shot{height:208px;background:linear-gradient(180deg,#f4f4f4,#e2e2e2)}
.card h3{font-family:"Roboto",Arial,sans-serif;font-weight:400;font-size:18px;margin-top:22px}
.card p{font-size:11px;color:#666;line-height:1.5;margin-top:10px;padding:0 6px;height:50px;overflow:hidden}
.card .btn{margin-top:16px;padding:8px 22px;font-size:12px;border-radius:16px}

/* seo text */
.seo{height:1086px;background:#f5f5f5;border-top:1px solid var(--line);padding-top:46px}
.seo h4{font-family:"Roboto",Arial,sans-serif;font-weight:500;font-size:15px;text-transform:uppercase;color:#444;line-height:1.4;margin:26px 0 14px}
.seo h4:first-child{margin-top:0}
.seo p{font-size:11px;color:#666;line-height:1.75;margin-bottom:10px}
.cols{column-count:2;column-gap:40px}

/* footer */
.footer{height:316px;background:var(--footer);color:#cfcfcf;padding-top:44px}
.footer .wrap{display:grid;grid-template-columns:310px 310px 190px 1fr;gap:10px}
.footer .brand-name{color:var(--white);font-size:20px}
.footer p{font-size:12px;line-height:1.6;margin-top:16px}
.footer h5{font-family:"Roboto",Arial,sans-serif;font-weight:400;font-size:17px;color:var(--white);text-transform:uppercase;margin-bottom:18px}
.contact-line{display:flex;gap:14px;font-size:12px;line-height:1.55;margin-bottom:16px}
.contact-line svg{flex:none;margin-top:2px}
.links a{display:block;font-size:12px;line-height:1.55}
.social{display:flex;gap:8px;margin-top:18px}
.social i{width:22px;height:22px;border-radius:50%;border:1px solid #9a9a9a}
.bottom{height:63px;background:var(--footer-deep);color:#999;font-size:12px;text-align:center;line-height:63px}
</style>
</head>
<body>

<div class="topbar">
  <div class="wrap">
    <span class="drop">Sicher Einkaufen</span>
    <span class="drop">Vorteile</span>
    <span class="drop">Beratung &amp; Kontakt</span>
    <div class="rating">
      <span class="star">★</span><span class="star">★</span><span class="star">★</span><span class="star">★</span><span class="star">★</span>
      <span>&nbsp;Lena Kramer (4.48/5.00)</span>
    </div>
    <span class="account">My Account ▾</span>
    <span class="cart"><svg width="14" height="14" viewBox="0 0 14 14"><path d="M1 2h2l2 7h6l2-5H4" fill="none" stroke="#fff" stroke-width="1.5"/><circle cx="6" cy="12" r="1" fill="#fff"/><circle cx="10" cy="12" r="1" fill="#fff"/></svg></span>
  </div>
</div>

<header class="header">
  <div class="wrap">
    <div class="brand">
      <span class="brand-mark"></span>
      <span class="brand-name">Brunnfeld<br>Bauwaren</span>
    </div>
    <div class="search">
      <span>Suchbegriff oder Artikelnummer</span>
      <i><svg width="16" height="16" viewBox="0 0 16 16"><circle cx="7" cy="7" r="5" fill="none" stroke="#fff" stroke-width="2"/><path d="M11 11l4 4" stroke="#fff" stroke-width="2"/></svg></i>
    </div>
    <div class="hotline">
      <span class="ph"><svg width="16" height="16" viewBox="0 0 16 16"><path d="M4 1l3 3-2 2c1 2 3 4 5 5l2-2 3 3-2 3C7 15 1 9 1 3z" fill="#fff"/></svg></span>
      <div><b>08152/740 318 0</b><small>Mon - Fri 9:00 to 6:00 p.m.</small></div>
    </div>
  </div>
</header>

<nav class="nav">
  <div class="wrap">
    <span class="item has-sub">Online Shop</span>
    <span class="item has-sub">Service</span>
    <span class="item sep">Standorte<span>|</span>Für Händler<span>|</span>Installateure</span>
    <div class="seals"><span class="seal"></span><span class="seal sq"></span></div>
  </div>
</nav>

<div class="usp">
  <div class="wrap">
    <span><svg width="12" height="10" viewBox="0 0 12 10"><path d="M1 5l3 3 7-7" fill="none" stroke="#fff" stroke-width="2"/></svg>Heizung inkl. Montage</span>
    <span><svg width="12" height="10" viewBox="0 0 12 10"><path d="M1 5l3 3 7-7" fill="none" stroke="#fff" stroke-width="2"/></svg>Festpreisangebot</span>
    <span><svg width="12" height="10" viewBox="0 0 12 10"><path d="M1 5l3 3 7-7" fill="none" stroke="#fff" stroke-width="2"/></svg>Kostenlos &amp; unverbindlich</span>
  </div>
</div>

<section class="hero">
  <div class="hero-photo" role="img" aria-label="Photo of a chimney sweep standing on a tiled roof beside a brick chimney under a clear sky"></div>
  <div class="hero-copy">
    <h1>SCHORNSTEIN</h1>
    <a class="btn" href="#">View more info</a>
  </div>
  <div class="dots"><i class="on"></i><i></i><i></i><i></i></div>
</section>

<section class="brands">
  <div class="wrap">
    <span>KORVA</span><span>Tellmo</span><span>BRASSIN</span><span>Nuvaro</span><span>pelto</span><span>HALDEX</span>
  </div>
</section>

<section class="features">
  <div class="wrap">
    <div class="feature">
      <div class="ring"><svg width="54" height="54" viewBox="0 0 54 54"><path d="M27 6c6 10 14 15 14 26a14 14 0 0 1-28 0c0-7 5-11 7-17 3 4 3 8 7 9-1-6-2-12 0-18z" fill="var(--orange)"/></svg></div>
      <h3>Mandatory heating supply<br>immediately!</h3>
      <p>Lorem ipsum dolor sit amet, consectetur adipiscing elit, sed do eiusmod tempor incididunt ut labore et dolore</p>
    </div>
    <div class="feature">
      <div class="ring"><svg width="54" height="54" viewBox="0 0 54 54"><path d="M10 44l20-20M34 8a9 9 0 0 0 10 12l-8 8-8-8z" fill="none" stroke="var(--orange)" stroke-width="5" stroke-linecap="round"/><path d="M10 10l34 34" stroke="var(--ink)" stroke-width="4" stroke-linecap="round"/></svg></div>
      <h3>More than 30 years<br>master quality!</h3>
      <p>Lorem ipsum dolor sit amet, consectetur adipiscing elit, sed do eiusmod tempor incididunt ut labore et dolore</p>
    </div>
    <div class="feature">
      <div class="ring"><svg width="54" height="54" viewBox="0 0 54 54"><rect x="8" y="12" width="38" height="34" rx="3" fill="none" stroke="var(--orange)" stroke-width="4"/><path d="M8 22h38M18 6v10M36 6v10" stroke="var(--orange)" stroke-width="4"/><path d="M16 30h6M26 30h6M16 38h6M26 38h6" stroke="var(--ink)" stroke-width="3"/></svg></div>
      <h3>New heating already from<br>39 € per month!</h3>
      <p>Lorem ipsum dolor sit amet, consectetur adipiscing elit, sed do eiusmod tempor incididunt ut labore et dolore</p>
    </div>
    <div class="feature">
      <div class="ring"><svg width="54" height="54" viewBox="0 0 54 54"><circle cx="27" cy="22" r="14" fill="none" stroke="var(--orange)" stroke-width="4"/><circle cx="27" cy="22" r="6" fill="var(--orange)"/><path d="M19 34l-5 14 7-3 4 6 2-14M35 34l5 14-7-3-4 6-2-14" fill="none" stroke="var(--ink)" stroke-width="3"/></svg></div>
      <h3>10 year warranty on your<br>new heater!</h3>
      <p>Lorem ipsum dolor sit amet, consectetur adipiscing elit, sed do eiusmod tempor incididunt ut labore et dolore</p>
    </div>
  </div>
</section>

<section class="how">
  <h2>SO FUNKTIONIERT'S</h2>
  <p class="sub">In wenigen Schritten zum richtigen Angebot für Ihre Sanierung</p>
  <div class="steps">
    <div class="step">
      <div class="disc"><svg width="52" height="52" viewBox="0 0 52 52"><rect x="6" y="8" width="40" height="28" rx="2" fill="none" stroke="#fff" stroke-width="4"/><path d="M18 44h16M26 36v8" stroke="#fff" stroke-width="4"/></svg></div>
      <p>Daten online eingeben</p>
    </div>
    <div class="arrow">›</div>
    <div class="step">
      <div class="disc"><svg width="52" height="52" viewBox="0 0 52 52"><path d="M6 26L26 8l20 18M12 22v22h28V22" fill="none" stroke="#fff" stroke-width="4"/><rect x="22" y="30" width="8" height="14" fill="#fff"/></svg></div>
      <p>Aufmaß und Beratung durch<br>Kundenberater</p>
    </div>
    <div class="arrow">›</div>
    <div class="step">
      <div class="disc"><svg width="52" height="52" viewBox="0 0 52 52"><rect x="10" y="6" width="32" height="40" rx="2" fill="none" stroke="#fff" stroke-width="4"/><path d="M17 18h18M17 26h18M17 34h10" stroke="#fff" stroke-width="3"/></svg></div>
      <p>Angebot von 2 flammkant<br>Handwerkern</p>
    </div>
    <div class="arrow">›</div>
    <div class="step">
      <div class="disc"><svg width="56" height="52" viewBox="0 0 56 52"><path d="M4 12h30v24H4zM34 20h10l8 8v8H34z" fill="none" stroke="#fff" stroke-width="4"/><circle cx="14" cy="40" r="5" fill="#fff"/><circle cx="42" cy="40" r="5" fill="#fff"/></svg></div>
      <p>Ausführung</p>
    </div>
  </div>
  <p class="cta">Jetzt unverbindlich eine Anfrage stellen!</p>
  <a class="btn" href="#">Anfrage stellen!</a>
</section>

<section class="products">
  <h2>OUR PRODUCTS</h2>
  <div class="grid">
    <div class="card">
      <div class="shot" role="img" aria-label="Product photo of a stainless steel chimney extension with a cowl"></div>
      <h3>Chimney Extension</h3>
      <p>Fireplace extensions configurable pro-duced made to measure and crafted to the highest standard.</p>
      <a class="btn" href="#">Watch now</a>
    </div>
    <div class="card">
      <div class="shot" role="img" aria-label="Product photo of a stainless steel fireplace door"></div>
      <h3>fireplace door</h3>
      <p>Fireplace doors and flush doors made of stainless steel in many sizes available. Best quality and durability at a fair</p>
      <a class="btn" href="#">Watch now</a>
    </div>
    <div class="card">
      <div class="shot" role="img" aria-label="Product photo of a dark freestanding wood stove with visible flames"></div>
      <h3>stove</h3>
      <p>Stoves with excellent price / performance ratio order free shipping online. Long-lasting quality and security for your</p>
      <a class="btn" href="#">Watch now</a>
    </div>
    <div class="card">
      <div class="shot" role="img" aria-label="Product photo of a cylindrical stainless steel chimney fan"></div>
      <h3>Chimney fans</h3>
      <p>Chimney fans for the perfect train in the chimney, Made in Germany for high performance with guaranteed</p>
      <a class="btn" href="#">Watch now</a>
    </div>
  </div>
</section>

<section class="seo">
  <div class="wrap">
    <h4>Stainless steel chimneys, chimney extensions, stovepipes and chimney accessories - at brunnfeld-bauwaren.de buy anything cheap</h4>
    <div class="cols">
      <p>Can I use a steel chimney for sale on the internet? This question you have probably never asked. For other products which is a matter of course, but with a stainless steel chimney you do not think first to the online shopping. There are all around the subject for several years various platforms steel chimney offer. However, these providers operate their web shop only incidentally. This is reflected in the poor usability and the partly very outdated technology of pages. Brunnfeld Bauwaren has gone a new way here. The goal was a pet shop for stainless steel chimneys and chimney accessories to put on their feet,</p>
      <p>which is composed not only professionally and according to the latest state of the art, but also gives you the security and usability that you are used to large online platforms in other sectors. With an efficient organization, modern technology and years of experience with the product steel chimney, this claim could be met. Best usability, certified privacy, quality products and expert advice by telephone round your shopping experience from brunnfeld-bauwaren.de.</p>
    </div>
    <h4>Steel chimney, chimney kit and stainless steel chimney - all from one source</h4>
    <div class="cols">
      <p>Whether you have a double-walled stainless steel chimney, a chimney restoration looking for your old brick fireplace or chimney kit for your home: here you will find it. In brunnfeld-bauwaren.de you can find a wide range of manufactured in Germany stainless steel chimneys manufacturer Vellmar. These chimneys are manufactured according to the latest production methods of high-quality V4A stainless steel and are subject to stringent quality specifications. The Vellmar GmbH grants you beyond a guarantee of 25 years on each in this online shop acquired steel chimney. Quite simply: security at the best price!</p>
      <p>And another tip: All chimneys can be wonderfully with a stovepipe connect Vellmar. Here there is a large range at kits, various lengths, colors and angles. In addition, more recently, insulated stovepipes are available. This double-walled furnace tubes reduce the distance that must be maintained to combustible materials to a minimum.</p>
    </div>
    <h4>Build chimney extension and cowl extension low self</h4>
    <p>Due to new regulations, the height of many existing chimneys is no longer enough. By structural changes in the environment or many other reasons, it may happen that a chimney extension is necessary. In this online store you will find chimney extensions in versions double or single wall. Each chimney extension is made by hand and can be configured exactly to measure. Here you buy a chimney extension for eternity.</p>
    <h4>Lightweight construction chimney F90 and a wall duct: fire protection at the highest level</h4>
    <p>A stainless steel chimney is an excellent subsequent exhaust pipe beside an already brick chimney in the building. But what if you do not like the look or you prefer to leave the chimney inside invisible disappear? But that is lightweight engineering chimney Vellmar predestined. In conjunction with a refractory wall bushing here you have the perfect duo for secure additional chimney.</p>
    <h4>Chimney cap, chimney cover and chimney cover plate stainless steel to measure</h4>
    <p>Older chimney heads are subject to heavy loads due to weather conditions. After many years of rain, sunshine, the cold and the heat chimneys tops are porous and begin to crumble. Then it is high time for a chimney cover plate and a chimney cover. In fireplace covers, there are the famous hood and Kessling disc. These models have proven themselves over many years and are also mounted on most buildings. In brunnfeld-bauwaren.de measure chimney covers made of stainless steel or copper with 25 years warranty.</p>
    <h4>Chimney fans, draft stabilizer, fire doors and other specialty products</h4>
    <p>Round this online shop you will also find many other products around the topic of chimney and exhaust technology. Here for example, would the chimney fan to call. A very important device, which allows you to increase the chimney draft electrically. Also from the category of tension control and draught regulation. These so-called secondary air devices regulate purely mechanical chimney draft. In some cases, may also include a flue gas damper are necessary. In addition to the thermal exhaust flap can be found here also motorized flue dampers, which may be necessary for cascade or chimneys with double occupancy. Is finally even the fireplace door to mention. This component have most of them installed in the chimney side. Find suitable replacement, it should be even rusted.</p>
    <p>Enjoy shopping, wishes you the team of brunnfeld-bauwaren.de</p>
  </div>
</section>

<footer class="footer">
  <div class="wrap">
    <div>
      <div class="brand"><span class="brand-mark"></span><span class="brand-name">Brunnfeld<br>Bauwaren</span></div>
      <p>Feldkamp Studio is run by husband and wife team, Jonas and Mara Feldkamp. Our mission is to give you the edge over your competitors with proven online marketing strategies.</p>
      <div class="social"><i></i><i></i><i></i><i></i><i></i><i></i></div>
    </div>
    <div>
      <h5>Contact us</h5>
      <div class="contact-line"><svg width="14" height="18" viewBox="0 0 14 18"><path d="M7 1a6 6 0 0 1 6 6c0 4-6 10-6 10S1 11 1 7a6 6 0 0 1 6-6z" fill="#cfcfcf"/><circle cx="7" cy="7" r="2" fill="#2a2a2a"/></svg><span>© 2011 - 2016 Ofenwerk Vertrieb GmbH<br>Lindenhofweg 7<br>80339 Munich Germany</span></div>
      <div class="contact-line"><svg width="14" height="14" viewBox="0 0 16 16"><path d="M4 1l3 3-2 2c1 2 3 4 5 5l2-2 3 3-2 3C7 15 1 9 1 3z" fill="#cfcfcf"/></svg><span>Phone : +49 89 412 7730</span></div>
      <div class="contact-line"><svg width="16" height="12" viewBox="0 0 16 12"><rect x="1" y="1" width="14" height="10" fill="none" stroke="#cfcfcf" stroke-width="1.5"/><path d="M1 1l7 6 7-6" fill="none" stroke="#cfcfcf" stroke-width="1.5"/></svg><span>info@brunnfeld-bauwaren.de</span></div>
    </div>
    <div>
      <h5>Quick links</h5>
      <div class="links"><a href="#">Frequently Asked</a><a href="#">questions</a><a href="#">revocation</a><a href="#">data protection</a><a href="#">Contact us</a><a href="#">glossary</a></div>
    </div>
    <div>
      <h5>Free consultation</h5>
      <div class="links"><a href="#">08152/740 318 0</a><a href="#">Mo. Fr. 09:00 to 18:00 -</a><a href="#">info@brunnfeld-bauwaren.de</a></div>
    </div>
  </div>
</footer>
<div class="bottom">Copyright 2016 | All Rights Reserved - Brunnfeld Bauwaren</div>

</body>
</html>
```